Northwind Trade Allies - Letterhead and Folder

I am looking for letterhead that uses the splash from the logo on the side of the page as well as some information from our website.

I am looking for a folder that is a fold out that has pockets to hold paper as well as a slits for a business card.

Website address is www.northwindtradeallies.example

Target Market(s)

Export of Agrifoods, commodities and emergency aid.
Supplying the world food security.

Requirements
Must have
• Use splash and logo, have information about company.
• Letterhead must have splash on a side not in the middle.
Nice to have
• Different pictures that what are provided.

```html
<!DOCTYPE html>
<html lang="en">
<head>
<meta charset="utf-8">
<title>Northwind Trade Allies – Presentation Folder</title>
<link rel="stylesheet" href="https://fonts.googleapis.com/css2?family=Cinzel:wght@600&family=Montserrat:wght@400;500&display=swap">
<style>
  :root {
    --stage: #e4e4e4;
    --paper: #ffffff;
    --accent-green: #8dc63f;
    --accent-dark: #6aa82e;
    --field-teal: #1d8a94;
    --field-deep: #16705f;
    --field-green: #3f7a2a;
    --field-yellow: #b8b53a;
    --ink: #333333;
    --ink-soft: #555555;
  }
  * { box-sizing: border-box; margin: 0; padding: 0; }
  html, body { width: 1200px; height: 847px; overflow: hidden; }
  body { background: var(--stage); position: relative; }

  .folder-spread {
    position: absolute; left: 50px; top: 44px;
    width: 1100px; height: 760px;
    background: var(--paper);
    box-shadow: 0 18px 40px rgba(0,0,0,.18);
    overflow: hidden;
  }
  .field-photo {
    position: absolute; inset: 0;
    background: linear-gradient(180deg,
      var(--field-teal) 18%, #1f8278 38%, var(--field-deep) 52%,
      var(--field-green) 70%, var(--field-yellow) 100%);
  }
  .header-band { position: absolute; inset: 0; width: 1100px; height: 760px; }
  .fold-line {
    position: absolute; left: 548px; top: 0; width: 4px; height: 100%;
    background: linear-gradient(90deg, rgba(0,0,0,0), rgba(0,0,0,.12), rgba(0,0,0,0));
  }

  .back-cover-contact {
    position: absolute; left: 140px; top: 48px;
    padding-left: 14px;
    border-left: 1.5px solid var(--accent-green);
    font-family: "Montserrat", sans-serif;
    font-size: 11px; line-height: 1.45; color: var(--ink-soft);
  }
  .contact-row { display: flex; align-items: flex-start; gap: 8px; }
  .contact-row svg { width: 10px; height: 10px; margin-top: 3px; flex: none; }
  .contact-row svg * { fill: none; stroke: var(--accent-green); stroke-width: 1.6; }
  .contact-row svg .solid { fill: var(--accent-green); stroke: none; }

  .front-cover-brand {
    position: absolute; left: 550px; top: 60px; width: 550px;
    display: flex; align-items: center; justify-content: center; gap: 14px;
  }
  .brand-dot {
    width: 48px; height: 48px; border-radius: 50%;
    border: 4px solid var(--accent-green);
  }
  .brand-name {
    font-family: "Cinzel", serif; font-weight: 600;
    font-size: 24px; letter-spacing: .5px; color: var(--ink);
  }
</style>
</head>
<body>
  <main class="folder-spread">
    <div class="field-photo" role="img" aria-label="Photograph of a flowering yellow canola field fading into a teal misty sky"></div>

    <svg class="header-band" viewBox="0 0 1100 760" aria-hidden="true">
      <path d="M0 0 H1100 V170 C820 172 360 185 0 240 Z" fill="var(--paper)"/>
      <path d="M1100 170 C820 172 360 185 0 240" fill="none" stroke="var(--accent-green)" stroke-width="6"/>
    </svg>

    <div class="fold-line" aria-hidden="true"></div>

    <address class="back-cover-contact">
      <div class="contact-row">
        <svg viewBox="0 0 10 10"><path class="solid" d="M2 0.5 L4 2.5 L3 4 Q4.5 6 6 7 L7.5 6 L9.5 8 L8 9.5 Q3 9 0.5 2 Z"/></svg>
        <span>555-214-7730</span>
      </div>
      <div class="contact-row">
        <svg viewBox="0 0 10 10"><rect x="1" y="2" width="8" height="6" rx="1"/><path d="M1 2.5 L5 5.5 L9 2.5"/></svg>
        <span>555-382-4169</span>
      </div>
      <div class="contact-row">
        <svg viewBox="0 0 10 10"><circle cx="5" cy="5" r="4"/><path d="M1 5 H9 M5 1 Q2.5 5 5 9 Q7.5 5 5 1"/></svg>
        <span>www.northwindtradeallies.example</span>
      </div>
      <div class="contact-row">
        <svg viewBox="0 0 10 10"><path class="solid" d="M5 0.5 A3.3 3.3 0 0 1 8.3 3.8 C8.3 6 5 9.5 5 9.5 C5 9.5 1.7 6 1.7 3.8 A3.3 3.3 0 0 1 5 0.5 Z"/></svg>
        <span>Northwind Trade Allies Ltd.<br>118-420 Harbour Rd. E<br>Lakeview, MB, R3X1P4</span>
      </div>
    </address>

    <div class="front-cover-brand">
      <span class="brand-dot" aria-hidden="true"></span>
      <span class="brand-name">NORTHWIND TRADE ALLIES</span>
    </div>
  </main>
</body>
</html>
```